Lumo4Kart - a fintech company - business card

We need a business card design for our Payments Technology company in Sydney, Australia. We provide business with payment solutions expanding across EFTPOS machines, online payment gateways and mobile payment solutions. We would like to see designs that are clean, classy and professional.
Target Market(s)
Business professionals, executives, c-suite
Industry/Entity Type
Fintech
Contact Information for Business Card
Will be on 400gsm. Logo will most likely be spot gloss unless designer recommends otherwise.
Font styles to use
Sans Serif
Requirements
Must have
- We need our website (lumo4kart.com.au), email (contact@lumo4kart.com.au), mobile (0432 587 904) and direct phone number (02 6815 3927) to feature on the card along with our logo (attached) and the words "EFTPOS | ONLINE | MOBILE"
- Font = Roboto

```html
<!DOCTYPE html>
<html lang="en">
<head>
<meta charset="utf-8">
<title>Lumo4Kart Business Card</title>
<link href="https://fonts.googleapis.com/css2?family=Roboto:wght@400;500;700&display=swap" rel="stylesheet">
<style>
  :root {
    --page-bg: #f4f4f4;
    --card-black: #121212;
    --gloss-dark: #2a2a2a;
    --brand-blue: #145f92;
    --tag-blue: #1d5f94;
    --card-white: #ffffff;
    --text-grey: #666666;
  }
  * { margin: 0; padding: 0; box-sizing: border-box; }
  html, body {
    width: 1200px;
    height: 900px;
    overflow: hidden;
    background: var(--page-bg);
    font-family: "Roboto", Arial, sans-serif;
  }
  .canvas { position: relative; width: 1200px; height: 900px; }

  .card { position: absolute; overflow: hidden; }

  .card-front {
    left: 305px; top: 98px; width: 590px; height: 337px;
    background: var(--card-black);
  }
  .front-mark {
    position: absolute; left: 233px; top: 59px;
    width: 132px; height: 132px; border-radius: 50%;
    background: var(--gloss-dark);
  }
  .front-name {
    position: absolute; left: 0; right: 0; top: 192px;
    text-align: center;
    font-size: 44px; font-weight: 700; letter-spacing: -0.5px;
    color: var(--gloss-dark);
  }
  .front-tagline {
    position: absolute; left: 0; right: 0; top: 240px;
    text-align: center;
    font-size: 17px; font-weight: 500; letter-spacing: 3.4px;
    color: var(--tag-blue);
  }

  .card-back {
    left: 307px; top: 466px; width: 586px; height: 336px;
    background: var(--card-white);
  }
  .back-band {
    position: absolute; left: 0; top: 0; bottom: 0; width: 290px;
    background: var(--brand-blue);
  }
  .back-details { position: absolute; left: 340px; top: 178px; }
  .back-name {
    font-size: 30px; font-weight: 700; color: var(--text-grey);
    margin-bottom: 11px; letter-spacing: 0.2px;
  }
  .contact-list { list-style: none; }
  .contact-item {
    display: flex; align-items: center;
    font-size: 16px; color: var(--text-grey);
    height: 23.5px;
  }
  .contact-icon {
    width: 14px; height: 14px; margin-right: 7px;
    fill: var(--brand-blue); flex: none;
  }
</style>
</head>
<body>
<div class="canvas">

  <section class="card card-front">
    <div class="front-mark"></div>
    <p class="front-name">LUMO4KART</p>
    <p class="front-tagline">EFTPOS | ONLINE | MOBILE</p>
  </section>

  <section class="card card-back">
    <div class="back-band"></div>
    <div class="back-details">
      <p class="back-name">LUMO4KART</p>
      <ul class="contact-list">
        <li class="contact-item">
          <svg class="contact-icon" viewBox="0 0 16 16" aria-hidden="true"><path d="M1 6c0-2 3-4 7-4s7 2 7 4v1h-4V5.5C10 5 9 4.8 8 4.8S6 5 5 5.5V7H1z"/><path d="M4 8h8l2 6H2z"/></svg>
          02 6815 3927
        </li>
        <li class="contact-item">
          <svg class="contact-icon" viewBox="0 0 16 16" aria-hidden="true"><path d="M5 1h6a1 1 0 0 1 1 1v12a1 1 0 0 1-1 1H5a1 1 0 0 1-1-1V2a1 1 0 0 1 1-1zm.5 1.5v10h5v-10zM8 13.2a.6.6 0 1 0 0 1.2.6.6 0 0 0 0-1.2z"/></svg>
          0432 587 904
        </li>
        <li class="contact-item">
          <svg class="contact-icon" viewBox="0 0 16 16" aria-hidden="true"><path d="M1 3h14v1.2L8 9 1 4.2z"/><path d="M1 5.8 8 10.6l7-4.8V13H1z"/></svg>
          contact@lumo4kart.com.au
        </li>
        <li class="contact-item">
          <svg class="contact-icon" viewBox="0 0 16 16" aria-hidden="true"><path d="M8 1a7 7 0 1 0 0 14A7 7 0 0 0 8 1zm0 1.5c.6 0 1.6 1.4 2 4H6c.4-2.6 1.4-4 2-4zM2.6 6.5h2c-.1.5-.1 1-.1 1.5s0 1 .1 1.5h-2a5.6 5.6 0 0 1 0-3zm3.4 3h4c-.4 2.6-1.4 4-2 4s-1.6-1.4-2-4zm5.4 0c.1-.5.1-1 .1-1.5s0-1-.1-1.5h2a5.6 5.6 0 0 1 0 3z"/></svg>
          www.lumo4kart.com.au
        </li>
      </ul>
    </div>
  </section>

</div>
</body>
</html>
```